Need Business Card for our Real Estate Business with Sales Executive's Picture

PANTONE 484 C ( RED)

PANTONE 2766 C ( BLUE

Industry/Entity Type

Real Estate

Contact Information for Business Card

Name, Mobile, email, & picture of Person
Agency Phone, address, Web address

Requirements
Must have
• Our Logo Colours, Agent Picture,

```html
<!DOCTYPE html>
<html lang="en">
<head>
<meta charset="utf-8">
<title>Meridian Real Estate — Business Card</title>
<link rel="stylesheet" href="https://fonts.googleapis.com/css2?family=Cinzel:wght@500&family=Questrial&display=swap">
<style>
  :root {
    --navy: #1e2a5e;
    --navy-deep: #172250;
    --red: #8a1522;
    --red-deep: #6f0f1b;
    --white: #ffffff;
    --paper: #f4f4f6;
    --stage: #e9e9ec;
    --photo-a: #9aa6c4;
    --photo-b: #dfe3ec;
  }
  * { box-sizing: border-box; margin: 0; padding: 0; }
  html, body { width: 1200px; height: 864px; overflow: hidden; }
  body {
    background: var(--stage);
    position: relative;
    font-family: "Questrial", "Century Gothic", sans-serif;
  }
  .card {
    position: absolute;
    top: 278px;
    width: 540px;
    height: 309px;
    overflow: hidden;
    box-shadow: 0 6px 18px rgba(0,0,0,.18);
  }
  .card--front { left: 40px; background: var(--paper); }
  .card--back  { left: 620px; background: var(--navy); }

  /* front */
  .front__top { position: absolute; inset: 0 0 auto 0; height: 122px; background: var(--white); }
  .front__body {
    position: absolute; left: 0; right: 0; top: 122px; bottom: 0;
    background: linear-gradient(180deg, var(--navy) 0%, var(--navy-deep) 100%);
  }
  .front__rule { position: absolute; left: 0; right: 0; top: 128px; height: 2px; background: var(--white); }
  .agent-photo {
    position: absolute; left: 46px; top: 8px; width: 112px; height: 104px;
    border-radius: 50%; border: 2px solid var(--navy);
    background: radial-gradient(circle at 50% 40%, var(--photo-b) 0%, var(--photo-a) 100%);
  }
  .agent-name {
    position: absolute; left: 300px; top: 96px;
    font-family: "Cinzel", serif; font-weight: 500; font-size: 19px;
    color: var(--red); letter-spacing: .5px;
  }
  .logo-box {
    position: absolute; left: 14px; top: 144px; width: 214px; height: 124px;
    background: var(--white);
    display: flex; align-items: center; justify-content: center;
  }
  .logo-name {
    font-family: "Cinzel", serif; font-weight: 500; font-size: 17px;
    color: var(--navy); letter-spacing: 1px; text-align: center; line-height: 1.3;
  }
  .contact-list { position: absolute; left: 290px; top: 146px; list-style: none; }
  .contact-list li {
    display: flex; align-items: center; gap: 8px;
    color: var(--white); font-size: 14.5px; height: 21px; letter-spacing: .3px;
  }
  .contact-list svg { width: 12px; height: 12px; flex: none; }
  .address {
    position: absolute; left: 290px; top: 240px;
    color: var(--white); font-size: 14.5px; line-height: 19px; letter-spacing: .3px;
  }

  /* back */
  .back__art { position: absolute; inset: 0; }
  .back__logo {
    position: absolute; left: 0; right: 0; top: 214px; text-align: center;
    font-family: "Cinzel", serif; font-weight: 500; font-size: 22px;
    color: var(--white); letter-spacing: 1.5px;
  }
</style>
</head>
<body>

  <section class="card card--front" aria-label="Business card front">
    <div class="front__top"></div>
    <div class="front__body"></div>
    <div class="front__rule"></div>
    <div class="agent-photo" role="img" aria-label="Portrait photo of the sales executive"></div>
    <p class="agent-name">DANIEL REYES</p>

    <div class="logo-box">
      <p class="logo-name">MERIDIAN<br>REAL ESTATE</p>
    </div>

    <ul class="contact-list">
      <li>
        <svg viewBox="0 0 24 24" fill="#fff" aria-hidden="true"><path d="M6.6 10.8a15.1 15.1 0 0 0 6.6 6.6l2.2-2.2c.3-.3.7-.4 1-.2 1.1.4 2.3.6 3.6.6.6 0 1 .4 1 1V20c0 .6-.4 1-1 1C10.6 21 3 13.4 3 4c0-.6.4-1 1-1h3.5c.6 0 1 .4 1 1 0 1.3.2 2.5.6 3.6.1.3 0 .7-.2 1z"/></svg>
        (08) 614 2270
      </li>
      <li>
        <svg viewBox="0 0 24 24" fill="none" stroke="#fff" stroke-width="2.4" aria-hidden="true"><rect x="6" y="2" width="12" height="20" rx="2"/><line x1="11" y1="18" x2="13" y2="18"/></svg>
        021 547 3096
      </li>
      <li>
        <svg viewBox="0 0 24 24" fill="none" stroke="#fff" stroke-width="2.2" aria-hidden="true"><rect x="2" y="5" width="20" height="14"/><polyline points="2,5 12,13 22,5"/></svg>
        daniel@meridianrealestate.com
      </li>
      <li>
        <svg viewBox="0 0 24 24" fill="none" stroke="#fff" stroke-width="2" aria-hidden="true"><circle cx="12" cy="12" r="10"/><ellipse cx="12" cy="12" rx="4.5" ry="10"/><line x1="2" y1="12" x2="22" y2="12"/></svg>
        www.meridianrealestate.com
      </li>
    </ul>
    <p class="address">2218 Lakeview Road Suite 410<br>Oak Ridge, Il 60092</p>
  </section>

  <section class="card card--back" aria-label="Business card back">
    <svg class="back__art" viewBox="0 0 540 309" preserveAspectRatio="none" aria-hidden="true">
      <defs>
        <linearGradient id="navyFade" x1="0" y1="0" x2="0" y2="1">
          <stop offset="0" stop-color="#1e2a5e"/>
          <stop offset="1" stop-color="#172250"/>
        </linearGradient>
      </defs>
      <rect width="540" height="309" fill="url(#navyFade)"/>
      <polygon points="0,0 540,0 540,150 0,72" fill="#8a1522"/>
      <polygon points="0,72 540,150 540,166 0,88" fill="#ffffff"/>
    </svg>
    <p class="back__logo">MERIDIAN REAL ESTATE</p>
  </section>

</body>
</html>
```